Business Card Design

We are a radiology group

We are working to move into new service centers

We want to communicate innovation and bringing our customers ahead with technology and outstanding results
Updates

I have uploaded a high resolution logo as requested :-)

Target Market(s)

hospitals, clinics

Industry/Entity Type

Business

Contact Information for Business Card

Deborah L. Pettigrew, MBA, CIIP
CTIO
deborah.pettigrew@tdrpc-mail.com
cell 518-476-2913
www.tdrpc-mail.com
Tidewater Diagnostic Radiology, PC

```html
<!DOCTYPE html>
<html lang="en">
<head>
<meta charset="utf-8">
<title>Tidewater Diagnostic Radiology – Business Card</title>
<link rel="stylesheet" href="https://fonts.googleapis.com/css2?family=Open+Sans:wght@400;600&display=swap">
<style>
  :root {
    --page-bg: #eceef0;
    --card-white: #ffffff;
    --teal-deep: #0a6f86;
    --teal-mid: #1592b0;
    --cyan-bright: #11b3e0;
    --ink-dark: #3d3f42;
    --ink-body: #4a4c50;
    --name-blue: #5fb8dc;
    --icon-blue: #3c8fc9;
    --card-shadow: rgba(0, 0, 0, 0.18);
  }
  * { box-sizing: border-box; margin: 0; padding: 0; }
  html, body {
    width: 1200px;
    height: 784px;
    overflow: hidden;
    background: var(--page-bg);
    font-family: "Open Sans", sans-serif;
  }
  .canvas {
    width: 1200px;
    height: 784px;
    display: flex;
    align-items: center;
    justify-content: center;
    gap: 48px;
  }
  .card {
    position: relative;
    width: 540px;
    height: 309px;
    border-radius: 4px;
    overflow: hidden;
    box-shadow: 0 6px 18px var(--card-shadow);
  }

  /* Front side */
  .card-front { background: var(--teal-deep); }
  .front-pattern {
    position: absolute;
    inset: 0;
    background:
      radial-gradient(ellipse at 85% 55%, var(--cyan-bright) 0%, rgba(17,179,224,0.55) 35%, rgba(17,179,224,0) 70%),
      linear-gradient(120deg, var(--teal-deep) 0%, var(--teal-mid) 55%, var(--cyan-bright) 100%);
  }
  .front-brand {
    position: absolute;
    left: 70px;
    top: 118px;
    color: var(--card-white);
    font-weight: 600;
    font-size: 22px;
    font-variant: small-caps;
    letter-spacing: 1.2px;
  }

  /* Back side */
  .card-back { background: var(--card-white); }
  .back-brand {
    position: absolute;
    left: 40px;
    top: 70px;
    color: var(--ink-dark);
    font-weight: 600;
    font-size: 22px;
    font-variant: small-caps;
    letter-spacing: 1.2px;
  }
  .person {
    position: absolute;
    left: 40px;
    top: 168px;
  }
  .person-name {
    color: var(--name-blue);
    font-size: 19px;
    font-weight: 400;
  }
  .person-title {
    color: var(--ink-body);
    font-size: 11px;
    margin-top: 1px;
    margin-left: 4px;
  }
  .contact-list {
    position: absolute;
    left: 40px;
    top: 226px;
    list-style: none;
  }
  .contact-item {
    display: flex;
    align-items: center;
    gap: 7px;
    color: var(--ink-body);
    font-size: 14px;
    line-height: 21px;
  }
  .contact-icon { width: 13px; height: 13px; flex: none; }
</style>
</head>
<body>
<main class="canvas">

  <section class="card card-front" aria-label="Card front">
    <div class="front-pattern" role="img" aria-label="Field of soft overlapping circles in teal and bright cyan"></div>
    <p class="front-brand">Tidewater Diagnostic Radiology</p>
  </section>

  <section class="card card-back" aria-label="Card back">
    <p class="back-brand">Tidewater Diagnostic Radiology</p>

    <div class="person">
      <p class="person-name">Deborah L. Pettigrew</p>
      <p class="person-title">MBA, CIIP CTIO</p>
    </div>

    <ul class="contact-list">
      <li class="contact-item">
        <svg class="contact-icon" viewBox="0 0 16 16" aria-hidden="true">
          <rect x="4" y="1" width="8" height="14" rx="1.5" fill="var(--icon-blue)"/>
          <rect x="5.3" y="3" width="5.4" height="8" fill="var(--card-white)"/>
          <circle cx="8" cy="13" r="0.9" fill="var(--card-white)"/>
        </svg>
        <span>518-476-2913</span>
      </li>
      <li class="contact-item">
        <svg class="contact-icon" viewBox="0 0 16 16" aria-hidden="true">
          <circle cx="8" cy="8" r="6.5" fill="none" stroke="var(--icon-blue)" stroke-width="1.4"/>
          <ellipse cx="8" cy="8" rx="2.8" ry="6.5" fill="none" stroke="var(--icon-blue)" stroke-width="1.2"/>
          <line x1="1.5" y1="8" x2="14.5" y2="8" stroke="var(--icon-blue)" stroke-width="1.2"/>
        </svg>
        <span>www.tdrpc-mail.com</span>
      </li>
      <li class="contact-item">
        <svg class="contact-icon" viewBox="0 0 16 16" aria-hidden="true">
          <rect x="1" y="3" width="14" height="10" rx="1" fill="var(--icon-blue)"/>
          <path d="M1.8 4 L8 9 L14.2 4" fill="none" stroke="var(--card-white)" stroke-width="1.3"/>
        </svg>
        <span>deborah.pettigrew@tdrpc-mail.com</span>
      </li>
    </ul>
  </section>

</main>
</body>
</html>
```